Poster Design Project

Need a design for a music festival called Counter-Lanternweek

The design needs to have areas for the following:
- Band Names
- DJ Names
- Sponsor Names and Logos
- Event location, Date & Time

Industry/Entity Type

Festival

```html
<!DOCTYPE html>
<html lang="en">
<head>
<meta charset="utf-8">
<title>Counter-Lanternweek</title>
<link rel="stylesheet" href="https://fonts.googleapis.com/css2?family=Arimo:wght@700&family=Kaushan+Script&display=swap">
<style>
  :root {
    --ink: #141414;
    --night: #000000;
    --deep-blue: #1b5f9e;
    --mid-blue: #2d8dd2;
    --sky-blue: #4cb2ec;
    --ice: #bfe6fb;
    --white: #ffffff;
    --sponsor-green: #2e6b3a;
  }
  html, body { margin: 0; padding: 0; overflow: hidden; background: var(--white); }
  .poster {
    position: relative;
    width: 899px;
    height: 1200px;
    overflow: hidden;
    font-family: "Arimo", Arial, sans-serif;
    background: linear-gradient(to bottom,
      var(--night) 0px, #05090e 250px, #163e63 330px,
      var(--sky-blue) 380px, #3fa4e4 560px, var(--mid-blue) 800px, var(--deep-blue) 1050px);
  }
  .page-curl { position: absolute; top: 0; right: 0; width: 330px; height: 120px; }
  .date {
    position: absolute; top: 12px; right: 26px; margin: 0;
    color: var(--white); font-size: 31px; font-weight: 700;
  }
  .date sup { font-size: 17px; }
  .ribbon { position: absolute; left: 80px; top: 140px; width: 740px; height: 180px; }
  .title {
    position: absolute; left: 110px; top: 170px; width: 680px; margin: 0;
    text-align: center; transform: rotate(-6deg);
    font-family: "Kaushan Script", cursive; font-weight: 400;
    font-size: 68px; line-height: 90px; color: var(--ink);
    text-shadow: 0 0 3px var(--white), 0 0 3px var(--white);
  }
  .notes-art {
    position: absolute; left: 0; top: 825px; width: 899px; height: 225px;
    background:
      radial-gradient(ellipse at 40% 100%, rgba(191,230,251,0.75), rgba(191,230,251,0) 60%),
      radial-gradient(ellipse at 80% 80%, rgba(120,200,245,0.6), rgba(120,200,245,0) 55%);
  }
  .time {
    position: absolute; top: 376px; left: 0; width: 100%; margin: 0;
    text-align: center; font-size: 56px; line-height: 64px; font-weight: 700; color: var(--ink);
  }
  .address {
    position: absolute; top: 456px; left: 0; width: 100%; margin: 0;
    text-align: center; font-size: 22px; line-height: 28px; font-weight: 700; color: var(--white);
  }
  .section-heading {
    position: absolute; left: 0; width: 100%; margin: 0;
    text-align: center; font-size: 34px; line-height: 40px; font-weight: 700; color: var(--ink);
  }
  .bands-heading { top: 540px; }
  .djs-heading { top: 870px; }
  .name-list {
    position: absolute; left: 40px; width: 819px; margin: 0;
    text-align: center; font-size: 23px; font-weight: 700; line-height: 55px;
    color: var(--white);
  }
  .band-list { top: 590px; }
  .dj-list { top: 915px; }
  .sponsor-strip {
    position: absolute; left: 0; top: 1050px; width: 899px; height: 150px;
    background: var(--white);
  }
  .sponsor {
    position: absolute; margin: 0; font-weight: 700; color: var(--ink);
    display: flex; align-items: center; gap: 10px;
  }
  .sponsor-crowdshift { left: 40px; top: 60px; font-size: 22px; }
  .sponsor-crowdshift .mark { width: 26px; height: 26px; background: var(--ink); }
  .sponsor-open { left: 350px; top: 63px; font-size: 22px; }
  .sponsor-resteasy { left: 590px; top: 54px; font-size: 32px; color: var(--sponsor-green); }
  .sponsor-resteasy .mark { width: 34px; height: 34px; background: var(--sponsor-green); }
</style>
</head>
<body>
<main class="poster">
  <svg class="page-curl" viewBox="0 0 330 120" aria-hidden="true">
    <defs>
      <linearGradient id="curlShade" x1="0" y1="0" x2="1" y2="1">
        <stop offset="0" stop-color="#3a3a3a"/>
        <stop offset="1" stop-color="#0c0c0c"/>
      </linearGradient>
    </defs>
    <path d="M0 0 H330 V120 C250 60 120 30 0 0 Z" fill="url(#curlShade)"/>
  </svg>
  <p class="date">Sept 15<sup>th</sup></p>

  <svg class="ribbon" viewBox="0 0 740 180" role="img" aria-label="Silver banner ribbon behind the festival title">
    <defs>
      <linearGradient id="silver" x1="0" y1="0" x2="0" y2="1">
        <stop offset="0" stop-color="#f4f4f4"/>
        <stop offset="0.5" stop-color="#b9bbbe"/>
        <stop offset="1" stop-color="#7d7f82"/>
      </linearGradient>
    </defs>
    <path d="M10 95 C130 75 220 60 350 55 C480 50 600 30 730 5 L730 90 C600 120 480 140 350 145 C220 150 130 160 10 175 Z" fill="url(#silver)"/>
  </svg>
  <h1 class="title">Counter-Lanternweek</h1>

  <div class="notes-art" role="img" aria-label="Swirling blue music notes illustration"></div>

  <p class="time">11:00A - Until</p>
  <p class="address">512 W. 48th St Riverton, NC 28999</p>

  <h2 class="section-heading bands-heading">THE BANDS</h2>
  <p class="name-list band-list">
    Paper Orchard ● Loud Theory ● Hale &amp; Wren Company<br>
    ● The Greyfoxes ● Nora Wakefield ● Paper Orchard<br>
    ● Loud Theory ● Hale &amp; Wren Company ● The Grey-<br>
    foxes ● Nora Wakefield ● Paper Orchard ● Loud Theory<br>
    ● Hale &amp; Wren Company ● The Greyfoxes ● Nora Wakefield
  </p>

  <h2 class="section-heading djs-heading">THE DJS</h2>
  <p class="name-list dj-list">
    DJ Halcyon ● Mira Vox ● Static Owl ● Juno Marsh<br>
    DJ Corvel ● Tessa Lune ● Night Relay ● DJ Brightwater
  </p>

  <footer class="sponsor-strip">
    <p class="sponsor sponsor-crowdshift"><span class="mark"></span>CROWDSHIFT.COM</p>
    <p class="sponsor sponsor-open">sponsor space</p>
    <p class="sponsor sponsor-resteasy"><span class="mark"></span>Rest Easy Youth</p>
  </footer>
</main>
</body>
</html>
```